Wohnhof am Weiher - Zeitungsinserat für den Verkauf von Eigentumswohnungen

Wir brauchen ein Zeitungsinserat in zwei Formaten. Einmal 296 Breite x 440 Höhe mm und einmal 296 Breite x 220 mm Höhe.
Als Basis dient der sehr grobe Entwurf im Powerpoint (Entwurf.pptx).
Auf dem Entwurf fehlen noch die Kontaktangeben:
Brunnhofer Liegenschaften AG
Seematteweg 14
4387 Tannried
079 462 37 58
rbrunnhofer@tessin-ostwald.ch

Zudem muss noch der Link auf die Webseite aufgeführt werden.
www.wohnhof-am-weiher.ch

Zudem fehlt noch der Text:
Fordern Sie noch heute die Verkaufsunterlagen gedruckt oder per Email an. Schreiben Sie uns einfach eine Chatpost mit Ihrer Adresse.

Ich habe noch Files von den Innenvisualisierungen, den Aussenvisualisierungen sowie unser Logo hinzugefügt. Zudem habe ich Ihnen die Verkaufsbrochure angefügt. Sie können die Daten vom Entwurf gerne ergänzen wenn Ihnen etwas gefällt. Schön wäre es, wenn Sie den Stil ähnlich machen würden wie die Brochure.

Target Market(s)

Famillien, Paare und Rentner

Font styles to use
Serif

Colors

Designer to choose colors to be used in the design.

Requirements
Must have
• Tolles Design das sofort anspricht!

```html
<!DOCTYPE html>
<html lang="de">
<head>
<meta charset="utf-8">
<title>Wohnhof am Weiher – Inserat</title>
<link rel="stylesheet" href="https://fonts.googleapis.com/css2?family=Outfit:wght@800&family=Lexend:wght@400;600;700&display=swap">
<style>
  :root {
    --stage: #0f5f7b;
    --paper: #ffffff;
    --red: #e31e24;
    --blue: #0a6f96;
    --navy: #0b4c6a;
    --ink: #3a3a3a;
    --line: #5a5a5a;
  }
  * { box-sizing: border-box; margin: 0; padding: 0; }
  html, body { width: 1200px; height: 900px; overflow: hidden; }
  body { background: var(--stage); font-family: "Lexend", sans-serif; color: var(--ink); }

  .ad {
    position: absolute; left: 292px; top: 10px;
    width: 615px; height: 880px;
    background: var(--paper); overflow: hidden;
  }
  .hero-art { position: absolute; left: 0; top: 0; }

  .brand {
    position: absolute; left: 428px; top: 46px; width: 170px;
    font-family: "Lexend", sans-serif; font-weight: 600;
    color: var(--blue); text-align: center; line-height: 1.1;
  }
  .brand-name { display: block; font-size: 20px; letter-spacing: 1.2px; }
  .brand-sub { display: block; font-size: 8.5px; letter-spacing: 2.6px; margin-top: 5px; }

  .headline {
    position: absolute; left: 43px; top: 78px;
    border-left: 2px solid var(--red); padding-left: 12px;
  }
  .title {
    font-family: "Outfit", sans-serif; font-weight: 800;
    font-size: 44px; line-height: 41px; color: var(--blue); letter-spacing: .5px;
  }
  .title .accent { color: var(--red); }
  .subtitle {
    position: absolute; left: 55px; top: 166px;
    font-size: 17px; line-height: 19px; color: #4a4a4a;
  }

  .features { position: absolute; left: 14px; top: 315px; width: 285px; }
  .feature {
    position: relative; height: 56px; margin-bottom: 6px; margin-left: 11px;
    padding: 10px 14px 0 25px; color: #fff;
    border-radius: 2px; background: var(--blue);
  }
  .feature:nth-child(even) { background: var(--navy); }
  .feature h3 { font-size: 6.8px; font-weight: 700; letter-spacing: .2px; line-height: 8.4px; }
  .feature h3.lead { font-size: 7.6px; }
  .feature p { font-size: 6.6px; line-height: 8.3px; }
  .feature.dense { padding-top: 5px; }
  .tick {
    position: absolute; left: -11px; top: 12px; width: 32px; height: 32px;
  }

  .house-title {
    position: absolute; font-family: "Outfit", sans-serif; font-weight: 800;
    font-size: 16px; color: var(--red); letter-spacing: .3px;
  }
  .units {
    position: absolute; border-collapse: collapse; width: 266px;
    font-size: 7.8px; text-align: center; color: #444;
  }
  .units td { border: 1px solid var(--line); height: 36.8px; line-height: 8.4px; padding: 0 2px; }
  .units .floor {
    width: 16px; background: var(--navy); color: #fff; padding: 0;
    font-size: 7px; letter-spacing: .3px;
  }
  .units .floor span { writing-mode: vertical-rl; transform: rotate(180deg); display: inline-block; }
  .units .rooms { width: 62px; }
  .units .area { width: 44px; }
  .units .outdoor { width: 80px; }
  .units .price { width: 62px; }

  .house-a { left: 328px; top: 405px; }
  .table-a { left: 328px; top: 433px; }
  .house-b { left: 26px; top: 628px; }
  .table-b { left: 27px; top: 656px; }
  .house-c { left: 328px; top: 628px; }
  .table-c { left: 328px; top: 656px; }

  .contact {
    position: absolute; left: 0; right: 0; top: 848px;
    text-align: center; font-size: 11px; line-height: 13px; color: #333;
  }
  .contact .hl { color: var(--blue); }
  .contact .sep { color: var(--red); }
</style>
</head>
<body>
<main class="ad">
  <svg class="hero-art" width="615" height="480" viewBox="0 0 615 480">
    <defs>
      <linearGradient id="exteriorTone" x1="0" y1="0" x2="0" y2="1">
        <stop offset="0" stop-color="#cfe0ee"/>
        <stop offset=".55" stop-color="#b9bdbd"/>
        <stop offset="1" stop-color="#7d8f6a"/>
      </linearGradient>
      <linearGradient id="interiorTone" x1="0" y1="0" x2="1" y2="1">
        <stop offset="0" stop-color="#f1f1ef"/>
        <stop offset="1" stop-color="#b8b6b0"/>
      </linearGradient>
    </defs>
    <g role="img" aria-label="Aussenvisualisierung der Wohnanlage mit Terrassen und Garten">
      <polygon points="227,0 615,0 615,183 442,262 227,280" fill="url(#exteriorTone)"/>
    </g>
    <g role="img" aria-label="Aussenvisualisierung mit Rotfilter, Weg mit Velofahrer">
      <polygon points="615,183 442,262 615,423" fill="#d31c22"/>
    </g>
    <polygon points="20,218 226,279 20,307" fill="var(--red)"/>
    <circle cx="388" cy="308" r="78" fill="#fff"/>
    <g role="img" aria-label="Innenvisualisierung Wohnbereich mit Essplatz">
      <circle cx="388" cy="308" r="72" fill="url(#interiorTone)"/>
    </g>
    <circle cx="461" cy="376" r="46" fill="#fff"/>
    <g role="img" aria-label="Innenvisualisierung Küche und Esstisch">
      <circle cx="461" cy="376" r="41" fill="#a9a8a3"/>
    </g>
  </svg>

  <div class="brand">
    <span class="brand-name">BRUNNHOFER</span>
    <span class="brand-sub">LIEGENSCHAFTEN AG</span>
  </div>

  <header class="headline">
    <h1 class="title">W<span class="accent">O</span>HNHOF AM<br>WEIHER</h1>
  </header>
  <p class="subtitle">Hochwertige und moderne<br>Eigentumswohnungen</p>

  <section class="features">
    <article class="feature">
      <svg class="tick" viewBox="0 0 32 32"><circle cx="16" cy="16" r="15" fill="var(--navy)" stroke="#fff" stroke-width="2"/><path d="M9 16l5 6 11-13" fill="none" stroke="#fff" stroke-width="3" stroke-linecap="round" stroke-linejoin="round"/></svg>
      <h3>BUS UND BAHN</h3>
      <p>Der Bahnhof von Mühlegg mit Zugverbindungen nach Seeburg (20 Minuten) und Delsmatt ist in wenigen Minuten mit dem Bus zu erreichen.</p>
    </article>
    <article class="feature">
      <svg class="tick" viewBox="0 0 32 32"><circle cx="16" cy="16" r="15" fill="var(--navy)" stroke="#fff" stroke-width="2"/><path d="M9 16l5 6 11-13" fill="none" stroke="#fff" stroke-width="3" stroke-linecap="round" stroke-linejoin="round"/></svg>
      <h3>SEEBURG - STADT</h3>
      <p>Der nahegelegene Bahnhof in Mühlegg verfügt über sehr gute Verbindungen nach Seeburg (20 Minuten), welche durch den Doppelspurausbau in den kommenden Jahren sogar noch weiter verbessert werden.</p>
    </article>
    <article class="feature">
      <svg class="tick" viewBox="0 0 32 32"><circle cx="16" cy="16" r="15" fill="var(--navy)" stroke="#fff" stroke-width="2"/><path d="M9 16l5 6 11-13" fill="none" stroke="#fff" stroke-width="3" stroke-linecap="round" stroke-linejoin="round"/></svg>
      <h3>AUTOBAHN</h3>
      <p>Die Wohnsiedlung ist ideal auch für den Individualverkehr erschlossen. Die Entfernung zur Autobahn J18 beträgt 12km und ist über Eschenau innerhalb von 15 Minuten erreichbar.</p>
    </article>
    <article class="feature dense">
      <svg class="tick" viewBox="0 0 32 32"><circle cx="16" cy="16" r="15" fill="var(--navy)" stroke="#fff" stroke-width="2"/><path d="M9 16l5 6 11-13" fill="none" stroke="#fff" stroke-width="3" stroke-linecap="round" stroke-linejoin="round"/></svg>
      <h3 class="lead">EINKAUFEN UND WEITERE DIENSTLEISTUNGEN</h3>
      <p>Durch die Nähe der Gemeindegrenze zwischen Mühlegg und Tannried liegen die Dorfzentren mit ihren Einkaufsmöglichkeiten (z.B. Talmatt Center Mühlegg sowie der Altstadt in Mühlegg) und Dienstleistungsangeboten in max. 2 Minuten Fahrtzeit oder in 10-15 Minuten Gehdistanz.</p>
    </article>
    <article class="feature">
      <svg class="tick" viewBox="0 0 32 32"><circle cx="16" cy="16" r="15" fill="var(--navy)" stroke="#fff" stroke-width="2"/><path d="M9 16l5 6 11-13" fill="none" stroke="#fff" stroke-width="3" stroke-linecap="round" stroke-linejoin="round"/></svg>
      <h3>ERHOLUNG IM GRÜNEN</h3>
      <p>Tannried erfüllt mit seinen Wäldern, dem eigenen Dorfberg dem Hohsteinkopf, den offenen Feldern, den Wander- und Velorouten und der ländlichen Ruhe alle Voraussetzungen, die ein Naherholungsgebiet begehrt machen.</p>
    </article>
  </section>

  <h2 class="house-title house-a">HAUS A</h2>
  <table class="units table-a">
    <tr><td class="floor"><span>ATTIKA</span></td><td class="rooms">4.5<br>Zimmer</td><td class="area">108m²</td><td class="outdoor">105m²<br>Sonnenterrasse</td><td class="price">945'000 CHF</td></tr>
    <tr><td class="floor" rowspan="2"><span>OBERGESCHOSS</span></td><td>3.5<br>Zimmer</td><td>81m²</td><td>16m² Balkon</td><td>754'800 CHF</td></tr>
    <tr><td>4.5<br>Zimmer</td><td>102m²</td><td>33m² Balkon</td><td>640'000 CHF</td></tr>
    <tr><td class="floor" rowspan="2"><span>ERDGESCHOSS</span></td><td>3.5<br>Zimmer</td><td>81m²</td><td>16m² gedeckter<br>Sitzplatz &amp;<br>eigener Garten</td><td>657'000 CHF</td></tr>
    <tr><td>4.5<br>Zimmer</td><td>102m²</td><td>33m² gedeckter<br>Sitzplatz &amp;<br>eigener Garten</td><td>765'000 CHF</td></tr>
  </table>

  <h2 class="house-title house-b">HAUS B</h2>
  <table class="units table-b">
    <tr><td class="floor"><span>ATTIKA</span></td><td class="rooms">4.5<br>Zimmer</td><td class="area">109m²</td><td class="outdoor">107m²<br>Sonnenterrasse</td><td class="price">965'000 CHF</td></tr>
    <tr><td class="floor" rowspan="2"><span>OBERGESCHOSS</span></td><td>2.5<br>Zimmer</td><td>69m²</td><td>14m² Balkon</td><td>550'000 CHF</td></tr>
    <tr><td>4.5<br>Zimmer</td><td>117m²</td><td>42m² Balkon</td><td>877'500 CHF</td></tr>
    <tr><td class="floor" rowspan="2"><span>ERDGESCHOSS</span></td><td>2.5<br>Zimmer</td><td>69m²</td><td>14m² gedeckter<br>Sitzplatz &amp;<br>eigener Garten</td><td>560'000 CHF</td></tr>
    <tr><td>4.5<br>Zimmer</td><td>117m²</td><td>42m² gedeckter<br>Sitzplatz &amp;<br>eigener Garten</td><td>889'000 CHF</td></tr>
  </table>

  <h2 class="house-title house-c">HAUS C</h2>
  <table class="units table-c">
    <tr><td class="floor"><span>ATTIKA</span></td><td class="rooms">4.5<br>Zimmer</td><td class="area">129m²</td><td class="outdoor">132m²<br>Sonnenterrasse</td><td class="price">1'125'000<br>CHF</td></tr>
    <tr><td class="floor" rowspan="2"><span>OBERGESCHOSS</span></td><td>5.5<br>Zimmer</td><td>143m²</td><td>43m² Balkon</td><td>1'058'000<br>CHF</td></tr>
    <tr><td>3.5<br>Zimmer</td><td>96m²</td><td>23m² Balkon</td><td>730'000 CHF</td></tr>
    <tr><td class="floor" rowspan="2"><span>ERDGESCHOSS</span></td><td>5.5<br>Zimmer</td><td>143m²</td><td>43m² gedeckter<br>Sitzplatz &amp;<br>eigener Garten</td><td>1'065'000<br>CHF</td></tr>
    <tr><td>3.5<br>Zimmer</td><td>96m²</td><td>23m² gedeckter<br>Sitzplatz &amp;<br>eigener Garten</td><td>740'000 CHF</td></tr>
  </table>

  <footer class="contact">
    <p>Brunnhofer Liegenschaften AG, Seematteweg 14, 4387 Tannried</p>
    <p>079 462 37 58 <span class="sep">|</span> rbrunnhofer@<span class="hl">tessin-ostwald</span>.ch <span class="sep">|</span> www.<span class="hl">wohnhof-am-weiher</span>.ch</p>
  </footer>
</main>
</body>
</html>
```